New Creative Busines Card

Hi Lead Designer,

How are you going?

I was hoping you can help me design the perfect business card for my new business. I have listed below some background information about the business and the concept to help with your design. I'm open to any form of creative ideas, but would like to have two types of colour schemes one dark color and one light.

I would like to have a dark set of design and a light (One design with one in black or dark background and one with light background to compare the contrast since the business card will be double sided one) I imagine this will be pretty easy to change the background of the design. Would prefer one side to have all the details and the other will just have a amazing logo (K7) to give it the finishing touch.

Feel free to email me if you have any questions.

Business Structure and design concepts:

Name of the business: K7 Advisory
Business: Dating agency and event management (Date night etc)
Concept: The main focus will be the K7 ( As some sort of a heart shape like logo) be creative
Details to include in the card will be general details like Name, Title: , Email, mobile, website (Contact details will be given later).

The rest of the idea is up to you, feel free to go crazy with your creative ideas.

Thank you for your help in advance, may the best candidate win~!

Target Market(s)

Target market will be Professional, Elegant, young and ambitious people.

Industry/Entity Type

Business

Requirements
Must have
• Focus on the K7 (as some sort of a heart shape logo). Since this is a double sides design would prefer on one side to focus on the just the K7 logo and the other side with a smaller version of the logo (with it or without) and all the details such as Name, Title, Mobile, Email, Website. Please have the design in landscape format.Not fuss with the Font as long as it is easy to read.
Nice to have
• Different Contrast in colours (keep it simple) one side dark colour scheme and one side light. Prefer to have 3-4 colours (not overwhelm with too many colours) to keep it simple and elegant.
Should not have
• Too colours, main focus is should be the K7 logo not the colours

```html
<!DOCTYPE html>
<html lang="en">
<head>
<meta charset="utf-8">
<title>K7 Advisory – Business Card</title>
<link href="https://fonts.googleapis.com/css2?family=Quicksand:wght@500;600&display=swap" rel="stylesheet">
<style>
  :root {
    --page: #e9e4de;
    --wood-light: #6a4630;
    --wood-mid: #4a2e1e;
    --wood-dark: #2c1a10;
    --band: rgba(18, 10, 6, 0.82);
    --panel: #f1f0ef;
    --plum: #6b3a4a;
    --text-light: #f4efe9;
    --text-soft: #d9cfc6;
  }
  * { margin: 0; padding: 0; box-sizing: border-box; }
  html, body {
    width: 1200px;
    height: 982px;
    overflow: hidden;
    background: var(--page);
    font-family: "Quicksand", sans-serif;
  }
  .sheet {
    position: relative;
    width: 1200px;
    height: 982px;
  }
  .card {
    position: absolute;
    left: 300px;
    width: 600px;
    height: 320px;
    overflow: hidden;
    box-shadow: 0 10px 28px rgba(0, 0, 0, 0.28);
  }
  .card--front { top: 100px; }
  .card--back { top: 540px; }
  .card__wood {
    position: absolute;
    inset: 0;
    background: linear-gradient(180deg, var(--wood-light) 0%, var(--wood-mid) 45%, var(--wood-dark) 100%);
  }
  .card--back .card__wood {
    background: linear-gradient(180deg, var(--wood-mid) 0%, var(--wood-light) 55%, var(--wood-mid) 100%);
  }
  .card__band {
    position: absolute;
    left: 0;
    right: 0;
    background: var(--band);
  }
  .card--front .card__band {
    top: 118px;
    height: 96px;
    box-shadow: 0 0 22px 8px rgba(0, 0, 0, 0.55);
  }
  .card--back .card__band {
    top: 30px;
    height: 200px;
    background: rgba(28, 18, 12, 0.78);
  }
  .brand-panel {
    position: absolute;
    left: 210px;
    top: 88px;
    width: 180px;
    height: 156px;
    background: var(--panel);
    display: flex;
    align-items: center;
    justify-content: center;
    box-shadow: 0 2px 6px rgba(0, 0, 0, 0.4);
  }
  .brand-panel__name {
    color: var(--plum);
    font-weight: 600;
    font-size: 24px;
    letter-spacing: 0.5px;
  }
  .details {
    position: absolute;
    left: 34px;
    top: 150px;
    color: var(--text-light);
  }
  .details__name {
    font-weight: 600;
    font-size: 28px;
    line-height: 1;
  }
  .details__tagline {
    font-weight: 500;
    font-size: 13px;
    color: var(--text-soft);
    margin-top: 6px;
  }
  .details__contacts {
    list-style: none;
    margin-top: 22px;
    font-weight: 500;
    font-size: 14px;
    line-height: 1.55;
  }
</style>
</head>
<body>
  <main class="sheet">
    <section class="card card--front" aria-label="Card front">
      <div class="card__wood" role="img" aria-label="Dark wooden plank texture"></div>
      <div class="card__band"></div>
      <div class="brand-panel">
        <span class="brand-panel__name">K7 Advisory</span>
      </div>
    </section>

    <section class="card card--back" aria-label="Card back">
      <div class="card__wood" role="img" aria-label="Dark wooden plank texture"></div>
      <div class="card__band"></div>
      <div class="details">
        <p class="details__name">K7 Advisory</p>
        <p class="details__tagline">Dating Agencies and Dating Managment</p>
        <ul class="details__contacts">
          <li>E-Mail : mail@k7advisory.com</li>
          <li>Mobile : 000-00-0000</li>
          <li>Website : www.k7advisoryagency.com</li>
        </ul>
      </div>
    </section>
  </main>
</body>
</html>
```